Web design for our new company

We need a web design for our product and for our company.
And the main is our Product tool called "velmora".
----------------------------------------------------------
[Our company's Goal]
Make organization’s communication smooth and healthy with transparency and efficiency for works and tasks in all levels with our workflow tool.

[Our Mission]
Our mission is to achieve business goals with customers.
We work together to identify the goals for your company, guides your strategy and bring the technology answers which best fit to achieve the goals.

[What we do]
We have a workflow tool "velmora"
- Very simple end-user configurable workflow for any company processes
(Targeting small-med size company)
- Graphical & fun features for startup users
- Simple and easy task control with quillbox e-mail look & feel
- Non charged skill up guidance
- Additional features with;
Multiple delegation
Clear status for each owner
Task owner management console with due date reminders&reporting

Others
1. System Development & Implementation Service
Our client list includes a wide variety of small to medium to major sized enterprises.
We can offer from full-scratch based development to packaged system implementation.

2. Project Management(PM) Service
We will provide end-to-end PM service with experienced PM.
Our service is not only “managing” but “leading” to bring success to achieve the goal.

3.Consultation Service

Consulting services to a wide range of fields such as creating business strategy, business process Kaizen, IT system consultation and change management.

Target Market(s)

Business to Business
Mainly to medium size - startup company

Industry/Entity Type

It Company

Coding

Coded - Design and coding required

Number of Pages Required

5+ page

Colors
0255a3
33a6d7
86cfc6
33b8a4
add136
cadf82
fbf289
fee18a
faa54b

Requirements
Must have
• We need Pages for
• Company mission
• Service Overview
• Contact
• Privacy Policy
• Terms and Conditions
• =========================
• As there were some questions, I add followings.---------
• 1. File Format
• We are going to use Brixel cloud services to upload finished web files.
• The finished files should be ready to use by simply replacing images and text.
• Please provide me "easy to handle" template with "sophisticated design".
• Thanks!
• 2. Multiple Languages
• We need buttons for changing language.
• We will have this translated to German, English and Japanese.
• Thank you so much!!
Nice to have
• These are current Logos and will be a next project to revise them...
• Attached Company Profile and Logo design
• 1. Company Profile
• 2. Our Company Logo
• 3. Our Product Logo -> This is most close to our image of design base.
• 4. Product Logo for PPT Header
• All just for your reference.
• ---------
• As there were some request, I added attachment as for contents for Our mission page.
Should not have
• I hope to see some unique designs.
• (Sorry please ignore my last update as I checked with our CEO.
• Bootstrap is absolutely good template.)

```html
<!DOCTYPE html>
<html lang="en">
<head>
<meta charset="utf-8">
<title>velmora — Business Goals with Customers</title>
<link rel="stylesheet" href="https://fonts.googleapis.com/css2?family=Raleway:wght@400;500;600;700&family=Open+Sans:wght@400;600&display=swap">
<style>
:root{
  --navy:#1f2530;
  --dark:#262b35;
  --footer:#141820;
  --blue:#33a6d7;
  --blue-deep:#2c8fc4;
  --lime:#add136;
  --green:#7cc242;
  --ink:#222;
  --muted:#6b6f76;
  --light:#b9bec7;
  --line:#e4e6ea;
}
*{box-sizing:border-box;margin:0;padding:0}
html,body{width:1200px;height:4027px;overflow:hidden}
body{font-family:"Open Sans",sans-serif;color:var(--ink);background:#fff;position:relative}
.head{font-family:"Raleway",sans-serif}
section{position:relative;width:1200px;overflow:hidden}
.photo{position:absolute}
.sec-title{font-family:"Raleway",sans-serif;font-weight:600;font-size:30px;letter-spacing:1.5px;text-align:center;color:var(--ink)}
.sec-rule{width:60px;height:2px;background:var(--lime);margin:14px auto 0}

/* hero */
.hero{height:636px}
.hero-photo{left:268px;top:0;width:932px;height:636px;background:linear-gradient(120deg,#e9edf1 0%,#cfd8e2 45%,#7d8ea3 75%,#3d4a5c 100%)}
.sidebar{position:absolute;left:0;top:0;width:268px;height:636px;background:var(--navy)}
.brand{position:absolute;left:40px;top:32px;width:82px;height:82px;background:#fff;display:flex;align-items:center;justify-content:center;font-family:"Raleway",sans-serif;font-weight:600;font-size:17px;color:var(--green)}
.nav{position:absolute;left:48px;top:158px;width:155px;list-style:none}
.nav li{display:flex;justify-content:space-between;align-items:center;height:44px;font-family:"Raleway",sans-serif;font-weight:700;font-size:12px;color:#fff;letter-spacing:.5px}
.nav li.active{color:var(--lime)}
.nav svg{width:7px;height:10px}
.follow{position:absolute;left:48px;top:486px;width:130px}
.follow .rule{height:1px;background:#59606b;margin-bottom:16px}
.follow p{font-size:13px;color:#cfd3d9;margin-bottom:12px}
.socials{display:flex;gap:10px}
.socials span{width:28px;height:28px;border:1.5px solid #fff;border-radius:50%}
.caption-top{position:absolute;left:352px;top:402px;padding:0 24px;height:60px;background:rgba(255,255,255,.92);font-family:"Raleway",sans-serif;font-size:28px;color:#333;line-height:60px}
.caption-main{position:absolute;left:360px;top:463px;width:680px;height:76px;background:var(--blue);font-family:"Raleway",sans-serif;font-weight:700;font-size:30px;letter-spacing:1px;color:#fff;line-height:76px;padding-left:38px}

/* mission */
.mission{height:524px;padding-top:70px}
.mission .lead{width:830px;margin:32px auto 0;text-align:center;font-size:13px;line-height:22px;color:var(--muted)}
.services{display:flex;justify-content:space-between;width:1020px;margin:42px auto 0}
.service{width:310px;text-align:center}
.service svg{width:60px;height:60px}
.service h3{font-family:"Raleway",sans-serif;font-weight:700;font-size:16px;margin:14px 0 14px}
.service p{font-size:12.5px;line-height:20px;color:var(--muted);width:250px;margin:0 auto}

/* why */
.why{height:494px;background:var(--dark)}
.why-bg{left:420px;top:0;width:780px;height:494px;background:linear-gradient(90deg,#262b35,#323846 60%,#2a303b)}
.why-photo{left:0;top:35px;width:537px;height:424px;background:linear-gradient(135deg,#b9c7d6 0%,#8ea2b8 40%,#5f6c7d 100%)}
.play{position:absolute;left:230px;top:210px;width:74px;height:74px;border-radius:50%;background:var(--blue);border:5px solid rgba(255,255,255,.7)}
.why-title{position:absolute;left:630px;top:90px;font-family:"Raleway",sans-serif;font-weight:700;font-size:20px;letter-spacing:1px;color:#fff}
.why-grid{position:absolute;left:635px;top:172px;display:grid;grid-template-columns:265px 265px;row-gap:40px}
.why-grid h4{font-family:"Raleway",sans-serif;font-weight:600;font-size:16px;color:var(--blue);margin-bottom:14px}
.why-grid p{font-size:12.5px;line-height:20px;color:var(--light);width:220px}

/* blog */
.blog{height:811px;padding-top:88px}
.feature{position:absolute;left:95px;top:193px;width:690px;height:505px;border:1px solid var(--line);background:#fff}
.feature-photo{left:0;top:0;width:688px;height:285px;background:linear-gradient(100deg,#7e7268,#cbc4bd 40%,#e8e6e3 65%,#a6adb5)}
.feature h3{position:absolute;left:30px;top:318px;font-family:"Raleway",sans-serif;font-weight:700;font-size:16px}
.feature p{position:absolute;left:30px;top:356px;width:580px;font-size:12.5px;line-height:20px;color:var(--muted)}
.meta{display:flex;align-items:center;gap:8px;font-size:9.5px;color:#555;letter-spacing:.3px}
.meta i{width:18px;height:18px;border-radius:50%;background:#c9b7a8;display:block}
.feature .meta{position:absolute;left:30px;top:451px}
.feature .plus{position:absolute;right:68px;top:440px;width:42px;height:42px;border-radius:50%;background:var(--blue)}
.feature .sep{position:absolute;left:0;right:0;top:490px;height:1px;background:var(--line)}
.side-list{position:absolute;left:818px;top:193px;width:340px}
.side-item{display:flex;gap:22px;height:128px}
.side-thumb{position:relative;width:117px;height:96px;background:linear-gradient(135deg,#c4ccd6,#7b8796)}
.side-item h4{font-family:"Raleway",sans-serif;font-weight:700;font-size:13px;line-height:18px;width:180px;margin:10px 0 12px}

/* clients quote */
.happy{height:456px}
.happy-photo{left:0;top:0;width:1200px;height:456px;background:linear-gradient(90deg,#6b4a3a 0%,#8c6550 30%,#5a4a42 55%,#3b3b3e 100%)}
.quote{position:absolute;left:583px;top:80px;width:507px;height:350px;background:rgba(38,43,53,.95);padding:50px 60px}
.quote h3{font-family:"Raleway",sans-serif;font-weight:500;font-size:30px;letter-spacing:1px;color:#fff}
.quote .rule{width:45px;height:2px;background:#fff;margin:18px 0 22px}
.quote p{font-style:italic;font-size:13px;line-height:20px;color:#d5d8dd}
.quote h5{font-family:"Raleway",sans-serif;font-weight:500;font-size:17px;letter-spacing:.5px;color:#fff;margin-top:22px}
.quote small{display:block;font-style:italic;font-size:12px;color:#cfd3d9;margin-top:6px}
.pager{position:absolute;right:52px;bottom:60px;width:92px;height:32px;border-radius:16px;background:var(--blue);display:flex;align-items:center;justify-content:center;gap:14px;color:#fff;font-size:13px}

/* logos */
.clients{height:320px;padding-top:82px}
.logo-row{display:flex;justify-content:center;gap:26px;margin-top:50px}
.logo-box{width:172px;height:100px;border:1px solid var(--line);display:flex;align-items:center;justify-content:center;font-family:"Raleway",sans-serif;font-weight:600;font-size:18px;color:#666}

/* cta */
.cta{height:282px;background:linear-gradient(90deg,rgba(51,166,215,.96),rgba(70,174,220,.9)),linear-gradient(90deg,#2a6e92,#4a90b5)}
.cta h2{font-family:"Raleway",sans-serif;font-weight:500;font-size:30px;line-height:38px;color:#12253a;text-align:center;margin-top:68px}
.cta-btn{position:absolute;left:475px;top:173px;width:250px;height:46px;border:2px solid #12253a;background:rgba(255,255,255,.15);font-family:"Raleway",sans-serif;font-weight:700;font-size:13px;letter-spacing:.5px;color:#12253a;text-align:center;line-height:42px}

/* footer */
.footer{height:504px;background:var(--footer);color:#9aa0a9}
.fcol{position:absolute;top:92px}
.fcol h4{font-family:"Raleway",sans-serif;font-weight:600;font-size:18px;color:#fff;margin-bottom:26px}
.fcol ul{list-style:none;font-size:13px;line-height:33px}
.contact li{display:flex;gap:14px;line-height:21px;margin-bottom:16px;width:245px}
.contact svg{flex:none;width:12px;height:12px;margin-top:4px}
.news p{font-size:12.5px;margin-bottom:14px}
.subscribe{display:flex;width:335px;height:44px}
.subscribe div{flex:1;background:#2a2f38;font-size:12px;color:#8d939c;display:flex;align-items:center;gap:10px;padding-left:16px}
.subscribe span{width:110px;background:var(--green);color:#fff;font-family:"Raleway",sans-serif;font-weight:700;font-size:12px;display:flex;align-items:center;justify-content:center}
.news h5{font-family:"Raleway",sans-serif;font-weight:600;font-size:18px;color:#fff;margin:40px 0 18px}
.circles{display:flex;gap:12px}
.circles span{width:34px;height:34px;border-radius:50%}
.footer .base{position:absolute;left:58px;right:58px;top:408px;height:1px;background:#2a2f38}
.footer .copy{position:absolute;left:0;right:0;top:445px;text-align:center;font-size:11px}
</style>
</head>
<body>

<section class="hero">
  <div class="photo hero-photo" role="img" aria-label="Photo of two colleagues reviewing charts at a bright office desk"></div>
  <aside class="sidebar">
    <div class="brand">velmora</div>
    <ul class="nav">
      <li class="active">HOME<svg viewBox="0 0 7 10"><path d="M1 1l4 4-4 4" stroke="currentColor" fill="none" stroke-width="1.5"/></svg></li>
      <li>SERVICE<svg viewBox="0 0 7 10"><path d="M1 1l4 4-4 4" stroke="currentColor" fill="none" stroke-width="1.5"/></svg></li>
      <li>ABOUT US<svg viewBox="0 0 7 10"><path d="M1 1l4 4-4 4" stroke="currentColor" fill="none" stroke-width="1.5"/></svg></li>
      <li>PRODUCT<svg viewBox="0 0 7 10"><path d="M1 1l4 4-4 4" stroke="currentColor" fill="none" stroke-width="1.5"/></svg></li>
      <li>PRICING<svg viewBox="0 0 7 10"><path d="M1 1l4 4-4 4" stroke="currentColor" fill="none" stroke-width="1.5"/></svg></li>
      <li>POLICY<svg viewBox="0 0 7 10"><path d="M1 1l4 4-4 4" stroke="currentColor" fill="none" stroke-width="1.5"/></svg></li>
      <li>CONTACT US<svg viewBox="0 0 7 10"><path d="M1 1l4 4-4 4" stroke="currentColor" fill="none" stroke-width="1.5"/></svg></li>
    </ul>
    <div class="follow">
      <div class="rule"></div>
      <p>Follow Us :</p>
      <div class="socials"><span></span><span></span><span></span><span></span></div>
    </div>
  </aside>
  <div class="caption-top">Our Mission is to Achieve</div>
  <div class="caption-main">BUSINESS GOALS WITH CUSTOMERS .</div>
</section>

<section class="mission">
  <h2 class="sec-title">OUR MISSION</h2>
  <div class="sec-rule"></div>
  <p class="lead">Our mission is to achieve business goals with customers. We work together to identify the goals for your company, guides your strategy and bring the technology answers which best fit to achieve the goals.</p>
  <div class="services">
    <div class="service">
      <svg viewBox="0 0 60 60" fill="none" stroke="#33a6d7" stroke-width="2"><rect x="12" y="10" width="32" height="40" rx="2"/><path d="M18 20h20M18 28h14M18 36h18"/><circle cx="46" cy="42" r="8"/><path d="M43 42l2 2 4-4"/></svg>
      <h3>Project Management(PM) Service</h3>
      <p>We will provide end-to-end PM service with experienced PM. Our service is not only <b>"Managing"</b> but <b>"Leading"</b> to bring success to achieve the goal.</p>
    </div>
    <div class="service">
      <svg viewBox="0 0 60 60" fill="none" stroke="#33a6d7" stroke-width="2"><rect x="10" y="16" width="28" height="34" rx="2"/><path d="M16 24h16M16 31h16M16 38h10"/><circle cx="44" cy="18" r="7"/><path d="M44 25v16M38 33h12M44 41l-5 9M44 41l5 9"/></svg>
      <h3>System Development &amp; Implementation</h3>
      <p>Our client list includes a wide variety of small to medium to major sized enterprises. We can offer from full-scratch based development to packaged system.</p>
    </div>
    <div class="service">
      <svg viewBox="0 0 60 60" fill="none" stroke="#33a6d7" stroke-width="2"><circle cx="30" cy="16" r="6"/><circle cx="14" cy="42" r="6"/><circle cx="46" cy="42" r="6"/><path d="M27 21l-10 16M33 21l10 16M20 42h20"/><circle cx="30" cy="34" r="4"/></svg>
      <h3>Consultation Service</h3>
      <p>Consulting services to a wide range of fields such as creating business strategy, business process Kaizen, IT system consultation and</p>
    </div>
  </div>
</section>

<section class="why">
  <div class="photo why-bg"></div>
  <div class="photo why-photo" role="img" aria-label="Photo of two coworkers discussing work at a laptop by a window"></div>
  <div class="play"><svg viewBox="0 0 64 64" width="64" height="64"><path d="M26 20l18 12-18 12z" fill="#fff"/></svg></div>
  <h2 class="why-title">WHY CHOOSE US</h2>
  <div class="why-grid">
    <div><h4>Customer Support</h4><p>There are many variations of passages of Lorem Ipsum but the majority have industrial forms</p></div>
    <div><h4>Bulk SMS</h4><p>All the Lorem Ipsum on the Internet tend to repeat predefined chunks necessary generators</p></div>
    <div><h4>Money Exchange</h4><p>There are many variations of passages of Lorem Ipsum but the majority have industrial forms</p></div>
    <div><h4>Business Boosting</h4><p>There are many variations of passages of Lorem Ipsum but the majority have industrial forms</p></div>
  </div>
</section>

<section class="blog">
  <h2 class="sec-title">LATEST BLOG</h2>
  <div class="sec-rule"></div>
  <article class="feature">
    <div class="photo feature-photo" role="img" aria-label="Photo of a coach and a client talking across a table"></div>
    <h3>Why Would a Successful Entrepreneur Hire a Coach?</h3>
    <p>Our mission is to achieve business goals with customers. We work together to identify the goals for your company, guides your strategy.</p>
    <div class="meta"><i></i>BY: ADMIN &nbsp;|&nbsp; FEB 15, 2017</div>
    <div class="plus"><svg viewBox="0 0 42 42" width="42" height="42"><path d="M21 14v14M14 21h14" stroke="#fff" stroke-width="2"/></svg></div>
    <div class="sep"></div>
  </article>
  <div class="side-list">
    <div class="side-item"><div class="side-thumb" role="img" aria-label="Thumbnail photo of a business meeting"></div><div><h4>Successful Entrepreneur Hire a Coach?</h4><div class="meta"><i></i>BY: ADMIN | FEB 15, 2017</div></div></div>
    <div class="side-item"><div class="side-thumb" role="img" aria-label="Thumbnail photo of a team at a laptop"></div><div><h4>Successful Entrepreneur Hire a Coach?</h4><div class="meta"><i></i>BY: ADMIN | FEB 15, 2017</div></div></div>
    <div class="side-item"><div class="side-thumb" role="img" aria-label="Thumbnail photo of colleagues talking"></div><div><h4>Successful Entrepreneur Hire a Coach?</h4><div class="meta"><i></i>BY: ADMIN | FEB 15, 2017</div></div></div>
    <div class="side-item"><div class="side-thumb" role="img" aria-label="Thumbnail photo of an office discussion"></div><div><h4>Successful Entrepreneur Hire a Coach?</h4><div class="meta"><i></i>BY: ADMIN | FEB 15, 2017</div></div></div>
  </div>
</section>

<section class="happy">
  <div class="photo happy-photo" role="img" aria-label="Photo of a smiling client standing before a brick wall"></div>
  <div class="quote">
    <h3>HAPPY CLIENTS</h3>
    <div class="rule"></div>
    <p>There are many variations of passages of Lorem Ipsum available majority have suffered alteration. There are many variations of passages of Lorem Ipsum.</p>
    <h5>CLARA WHITFIELD</h5>
    <small>Harbor Town, Your Country</small>
    <div class="pager"><span>‹</span><span>›</span></div>
  </div>
</section>

<section class="clients">
  <h2 class="sec-title">OUR CLIENTS</h2>
  <div class="sec-rule"></div>
  <div class="logo-row">
    <div class="logo-box">Norvale</div>
    <div class="logo-box">Crestline</div>
    <div class="logo-box">Ardent Finance</div>
    <div class="logo-box">Tallis Finance</div>
    <div class="logo-box">Meridane</div>
  </div>
</section>

<section class="cta">
  <h2>Our Mission is to Achieve Business<br>Goals with Customers</h2>
  <div class="cta-btn">WORK WITH US TODAY</div>
</section>

<footer class="footer" style="position:relative">
  <div class="fcol contact" style="left:58px">
    <h4>Contact Us</h4>
    <ul>
      <li><svg viewBox="0 0 12 12"><path d="M11 1L1 5l4 2 2 4z" fill="#fff"/></svg>12 Lindell Road, Suite 4B, Harbor Town, Your Country</li>
      <li><svg viewBox="0 0 12 12"><rect x="1" y="2" width="10" height="8" rx="1" fill="none" stroke="#fff"/></svg>(555) 014 2290 | (555) 014 7781</li>
      <li><svg viewBox="0 0 12 12"><rect x="1" y="2" width="10" height="8" fill="none" stroke="#fff"/><path d="M1 2l5 4 5-4" fill="none" stroke="#fff"/></svg>hello@velmora.example</li>
      <li><svg viewBox="0 0 12 12"><circle cx="6" cy="6" r="5" fill="#fff"/><path d="M6 3v3h2" stroke="#141820" fill="none"/></svg>Monday - Friday 09:30 - 18:00 Saturday, Sunday Closed</li>
    </ul>
  </div>
  <div class="fcol" style="left:340px">
    <h4>Quick Link</h4>
    <ul><li>About us</li><li>Services</li><li>Career</li><li>Projects</li><li>Blog</li><li>Contact</li></ul>
  </div>
  <div class="fcol" style="left:527px">
    <h4>Services</h4>
    <ul><li>Customer Support</li><li>Bulk sms service</li><li>Business boosting</li><li>Money exchange</li><li>Consulting Services</li><li>Strategic Planning</li><li>International</li></ul>
  </div>
  <div class="fcol news" style="left:805px">
    <h4>Newsletter</h4>
    <p>Enter your email &amp; subscribe newsletter</p>
    <div class="subscribe"><div><svg viewBox="0 0 12 12" width="12" height="12"><rect x="1" y="2" width="10" height="8" fill="none" stroke="#7cc242"/></svg>Email address</div><span>SUBSCRIBE</span></div>
    <h5>Contact us on</h5>
    <div class="circles">
      <span style="background:#3b5998"></span><span style="background:#4a76a8"></span><span style="background:#dd4b39"></span><span style="background:#e4405f"></span><span style="background:#1da1f2"></span>
    </div>
  </div>
  <div class="base"></div>
  <p class="copy">2018 all rights reserved</p>
</footer>

</body>
</html>
```